Electrical panel service sticker w Bucket truck & Logo

We have a rather plain sticker we put on lighting panels to remind customers who to call for service. We want to redesign them with brushed aluminum background. We want a remake of the sticker with the outline of a bucket truck. You'll need to find or draw the outling of a bucket truck maybe with the boom up slightly as we will get these stickers die cut.

We want LOGO with Ph.# and Email.
Electrical * Lighting * Sign Service

Target Market(s)

Commercial property managers

Industry/Entity Type

Property Management

Requirements
Must have
• Bucket Truck Outline

```html
<!DOCTYPE html>
<html lang="en">
<head>
<meta charset="utf-8">
<title>Panel Service Sticker</title>
<link rel="stylesheet" href="https://fonts.googleapis.com/css2?family=Saira:wght@500;600;700&display=swap">
<style>
  :root {
    --navy: #283887;
    --brick: #a01d22;
    --ink: #0d0d0d;
    --paper: #ffffff;
    --rule: #b4b4b4;
    --stage: #e9e7e3;
  }
  html, body {
    margin: 0;
    width: 1200px;
    height: 1200px;
    overflow: hidden;
    background: var(--stage);
    font-family: "Saira", sans-serif;
  }
  .sticker {
    position: absolute;
    left: 217px;
    top: 68px;
    width: 769px;
    height: 1065px;
    background: var(--paper);
    overflow: hidden;
  }
  .services {
    position: absolute;
    inset: 0 0 auto 0;
    height: 247px;
    background: var(--navy);
    color: var(--paper);
    font-weight: 600;
    font-size: 64px;
    line-height: 96px;
    text-align: center;
    padding-top: 26px;
    box-sizing: border-box;
    letter-spacing: -0.5px;
  }
  .services p { margin: 0; white-space: nowrap; }
  .brand {
    position: absolute;
    top: 318px;
    left: 0;
    right: 0;
    text-align: center;
    color: var(--brick);
    font-weight: 700;
    font-size: 74px;
    line-height: 84px;
    text-transform: uppercase;
    letter-spacing: -1px;
  }
  .brand p { margin: 0; white-space: nowrap; }
  .contact-label {
    position: absolute;
    top: 585px;
    left: 0; right: 0;
    text-align: center;
    color: var(--ink);
    font-weight: 600;
    font-size: 48px;
    line-height: 52px;
  }
  .phone {
    position: absolute;
    top: 630px;
    left: 0; right: 0;
    text-align: center;
    color: var(--ink);
    font-weight: 600;
    font-size: 84px;
    line-height: 84px;
    letter-spacing: 4px;
  }
  .divider {
    position: absolute;
    top: 743px;
    left: 69px;
    width: 630px;
    height: 3px;
    background: linear-gradient(90deg, transparent, var(--rule) 8%, var(--rule) 92%, transparent);
    border-radius: 2px;
  }
  .email {
    position: absolute;
    top: 777px;
    left: 0; right: 0;
    text-align: center;
    color: var(--ink);
    font-weight: 600;
    font-size: 41px;
    line-height: 48px;
    white-space: nowrap;
    letter-spacing: -0.3px;
  }
  .tagline-band {
    position: absolute;
    left: 0; right: 0; bottom: 0;
    height: 200px;
    background: var(--brick);
  }
  .truck-art {
    position: absolute;
    left: 33px;
    top: 32px;
    width: 196px;
    height: 132px;
    background: linear-gradient(135deg, #c0383d, #8a1519);
    border-radius: 4px;
  }
  .tagline {
    position: absolute;
    left: 258px;
    top: 44px;
    color: var(--paper);
    font-weight: 600;
    font-size: 46px;
    line-height: 58px;
    white-space: nowrap;
    letter-spacing: -0.3px;
  }
  .tagline p { margin: 0; }
</style>
</head>
<body>
  <main class="sticker">
    <header class="services">
      <p>ELECTRICAL • LIGHTING</p>
      <p>• SIGN SERVICE</p>
    </header>

    <div class="brand">
      <p>Brightline</p>
      <p>Upkeep Inc.</p>
    </div>

    <div class="contact-label">Call or Text</div>
    <div class="phone">877.555.0142</div>
    <div class="divider"></div>
    <div class="email">Service@BrightlineUpkeep.com</div>

    <footer class="tagline-band">
      <div class="truck-art" role="img" aria-label="White outline illustration of a bucket truck with its boom raised"></div>
      <div class="tagline">
        <p>TRUSTED &amp; RELIABLE</p>
        <p>LIGHTING EXPERTS</p>
      </div>
    </footer>
  </main>
</body>
</html>
```